Meridale Cleaning Services

In need of a business card design suited for a growing cleaning company.

We offer our cleaning and maintenance services to a wide range of clients including but not limited to the following: constuction industry, hospitality, commercial, industrial and domestic

I want the card to be very noticable, i would like people to say 'hey, great card!' when i hand them my card.double sided would be nice

we want our business to come across as exceedingly professional and innovative (different).

a contemporary design is what we have in mind
we want to present an image of a quality business with a high standard of excellence in consistent service.

i just really need a card that persuades top end quality,
our business is very certified and also strives towards environmentaly friendly alternatives
Updates

hey sorry, i have uploaded my company logo design and name
cheers.

hey guys i have added my company logo/name file on my brief page. many thanks

sorry guys a typo in the brief..
address is Tolley Rd. not Tolly Rd
thanks

Industry/Entity Type

Industrial

Requirements
Must have
• company name: meridale cleaning services
operations manager: Colm Varetti
Tel: (02)9373 6204
Fax: (02)8645 7712
Mob: 0438571490

address: 47 Tolly RD Pymble NSW 2073
Postal Adress: PO Box 5832 North Ryde NSW 2113
email: meridaleclean@wexanet.com.au
website: meridalecleaningservices.com.au

```html
<!DOCTYPE html>
<html lang="en">
<head>
<meta charset="utf-8">
<title>Meridale Cleaning Services – Business Card</title>
<link rel="stylesheet" href="https://fonts.googleapis.com/css2?family=Arimo:wght@400;700&display=swap">
<style>
  :root {
    --backdrop: #c9c9c9;
    --card-edge: #e6e6e6;
    --logo-panel: #ffffff;
    --accent-green: #6cbf3a;
    --accent-green-dark: #4fa12b;
    --blue-light: #2eaae2;
    --blue-mid: #1f86d0;
    --blue-deep: #1a58ad;
    --brand-blue: #1d6db6;
    --text-white: #ffffff;
    --text-role: #c4d3e6;
  }
  * { margin: 0; padding: 0; box-sizing: border-box; }
  html, body {
    width: 1200px;
    height: 720px;
    overflow: hidden;
    background: var(--backdrop);
    font-family: "Arimo", Arial, sans-serif;
  }
  .card {
    position: absolute;
    left: 43px;
    top: 38px;
    width: 1118px;
    height: 644px;
    overflow: hidden;
    border: 2px solid var(--card-edge);
    background:
      linear-gradient(90deg,
        var(--logo-panel) 0, var(--logo-panel) 254px,
        var(--accent-green) 254px, var(--accent-green-dark) 290px,
        transparent 290px),
      linear-gradient(115deg, var(--blue-light) 20%, var(--blue-mid) 55%, var(--blue-deep) 100%);
  }
  /* Content reads bottom-to-top along the card */
  .card__content {
    position: absolute;
    left: 237px;
    top: -237px;
    width: 644px;
    height: 1118px;
    transform: rotate(-90deg);
    transform-origin: center;
  }
  .brand {
    position: absolute;
    left: 40px;
    top: 0;
    height: 254px;
    display: flex;
    align-items: center;
    gap: 30px;
  }
  .brand__mark {
    width: 120px;
    height: 120px;
    border-radius: 50%;
    background: var(--brand-blue);
    flex-shrink: 0;
  }
  .brand__name {
    color: var(--brand-blue);
    font-weight: 700;
    font-size: 44px;
    line-height: 52px;
    max-width: 420px;
  }
  .person {
    position: absolute;
    left: 44px;
    top: 368px;
  }
  .person__name {
    color: var(--text-white);
    font-weight: 700;
    font-size: 40px;
    line-height: 44px;
  }
  .person__role {
    color: var(--text-role);
    font-size: 36px;
    line-height: 42px;
    margin-top: 2px;
  }
  .details {
    position: absolute;
    left: 44px;
    color: var(--text-white);
    font-size: 29px;
    line-height: 42px;
    list-style: none;
  }
  .details--address { top: 618px; }
  .details--phone { top: 815px; }
  .details--online { top: 1010px; }
</style>
</head>
<body>
  <div class="card">
    <div class="card__content">
      <div class="brand">
        <span class="brand__mark"></span>
        <p class="brand__name">Meridale Cleaning Services</p>
      </div>

      <div class="person">
        <p class="person__name">Colm Varetti</p>
        <p class="person__role">operations manager</p>
      </div>

      <ul class="details details--address">
        <li>47 Tolley RD Pymble NSW 2073</li>
        <li>PO Box 5832 North Ryde NSW 2113</li>
      </ul>

      <ul class="details details--phone">
        <li>Tel:&nbsp; (02) 9373 6204</li>
        <li>Fax: (02) 8645 7712</li>
        <li>Mob: 043 857 1490</li>
      </ul>

      <ul class="details details--online">
        <li>meridaleclean@wexanet.com.au</li>
        <li>meridalecleaningservices.com.au</li>
      </ul>
    </div>
  </div>
</body>
</html>
```